ridgeline paving card makeover

were a excavation/paving contractor from Monterey ca, I'm looking to have a card designed front and back that has company details on the front and a list of the services we offer on the back.

Target Market(s)

home owners property management companies

Industry/Entity Type

Contractor

Contact Information for Business Card

ridgeline paving 418 alder way Monterey ca. licensed, insured and bonded
lic#736920 gerald okafor operations manager

Font styles to use
Serif
Sans Serif

Colors
f78f20

Requirements
Must have
• a list of my services on back, asphalt construction and maintenance, drainage, foundations, retaining walls, chip seals, excavation, grading, landscape ground work, interlocking paver, hydro-seeding, structured and driveway demolition, utility trenching and stump removal.
Nice to have
• my new domain and page address I'm acquiring from brief forge.

```html
<!DOCTYPE html>
<html lang="en">
<head>
<meta charset="utf-8">
<title>Ridgeline Paving — Business Card</title>
<link href="https://fonts.googleapis.com/css2?family=Roboto+Condensed:wght@400;700&family=Roboto+Slab:wght@800&display=swap" rel="stylesheet">
<style>
  :root {
    --orange: #f78f20;
    --black: #0d0d0d;
    --ink: #151515;
    --white: #ffffff;
    --stage: #2a2a2a;
  }
  * { box-sizing: border-box; margin: 0; padding: 0; }
  html, body { width: 1200px; height: 900px; overflow: hidden; }
  body {
    background: var(--stage);
    font-family: "Roboto Condensed", Arial, sans-serif;
    position: relative;
  }
  .card {
    position: absolute;
    left: 250px;
    width: 700px;
    height: 400px;
    background: var(--black);
    overflow: hidden;
    color: var(--white);
  }
  .card-front { top: 30px; }
  .card-back { top: 470px; }
  .card-shapes { position: absolute; inset: 0; }

  /* front */
  .holder { position: absolute; left: 40px; top: 26px; }
  .holder-name {
    font-family: "Roboto Slab", Georgia, serif;
    font-weight: 800;
    font-size: 40px;
    color: var(--ink);
    text-transform: uppercase;
    letter-spacing: 1px;
    line-height: 1;
  }
  .holder-title {
    font-size: 19px;
    letter-spacing: 7px;
    color: var(--white);
    text-transform: uppercase;
    margin-top: 8px;
  }
  .contact-list { position: absolute; left: 40px; top: 150px; list-style: none; }
  .contact-item {
    display: flex; align-items: center; gap: 12px;
    font-size: 20px; line-height: 26px; margin-bottom: 10px;
    white-space: nowrap;
  }
  .contact-icon {
    width: 28px; height: 28px; border-radius: 50%;
    background: var(--orange);
    display: flex; align-items: center; justify-content: center;
    flex: none;
  }
  .web-address {
    position: absolute; right: 34px; bottom: 14px;
    display: flex; align-items: center; gap: 10px;
    font-size: 24px; line-height: 28px; font-weight: 700; color: var(--ink);
    text-transform: uppercase; letter-spacing: 1px;
  }
  .web-dot { width: 18px; height: 18px; border-radius: 50%; border: 3px solid var(--ink); flex: none; }

  .brand-mark {
    position: absolute; display: flex; align-items: center; gap: 12px;
    font-weight: 700; font-size: 30px; color: var(--white);
    text-transform: uppercase; letter-spacing: 1px; line-height: 1.05;
  }
  .card-front .brand-mark { left: 480px; top: 170px; }
  .brand-dot { width: 34px; height: 34px; border-radius: 50%; background: var(--ink); flex: none; }

  /* back */
  .services-heading {
    position: absolute; left: 36px; top: 68px;
    color: var(--orange); font-size: 20px; letter-spacing: 2px;
    text-transform: uppercase;
  }
  .services-list { position: absolute; left: 36px; top: 104px; list-style: none; }
  .service {
    display: flex; align-items: center; gap: 10px;
    font-size: 16px; line-height: 20px; text-transform: uppercase; letter-spacing: 0.5px;
  }
  .service::before {
    content: ""; width: 10px; height: 10px; border-radius: 50%;
    background: var(--orange); border: 2px solid var(--black);
    box-shadow: 0 0 0 1px var(--orange); flex: none;
  }
  .card-back .brand-mark { left: 440px; top: 220px; }
  .card-back .brand-dot { background: var(--orange); }
</style>
</head>
<body>

<section class="card card-front" aria-label="Card front">
  <svg class="card-shapes" viewBox="0 0 700 400" aria-hidden="true">
    <path d="M0 0 H700 V320 H460 V130 H0 Z" fill="var(--orange)"/>
    <path d="M0 386 H310 C335 386 335 344 365 344 H700 V400 H0 Z" fill="var(--white)"/>
  </svg>

  <div class="holder">
    <h1 class="holder-name">Gerald Okafor</h1>
    <p class="holder-title">Managing Director</p>
  </div>

  <ul class="contact-list">
    <li class="contact-item">
      <span class="contact-icon"><svg width="15" height="15" viewBox="0 0 24 24"><path d="M6.6 10.8a15 15 0 0 0 6.6 6.6l2.2-2.2c.3-.3.7-.4 1-.2 1.1.4 2.3.6 3.6.6.6 0 1 .4 1 1V20c0 .6-.4 1-1 1A17 17 0 0 1 3 4c0-.6.4-1 1-1h3.5c.6 0 1 .4 1 1 0 1.3.2 2.5.6 3.6.1.3 0 .7-.2 1z" fill="#0d0d0d"/></svg></span>
      0491 337 204
    </li>
    <li class="contact-item">
      <span class="contact-icon"><svg width="12" height="16" viewBox="0 0 14 22"><rect x="1" y="1" width="12" height="20" rx="2" fill="none" stroke="#0d0d0d" stroke-width="2"/><circle cx="7" cy="17" r="1.4" fill="#0d0d0d"/></svg></span>
      0491 337 204
    </li>
    <li class="contact-item">
      <span class="contact-icon"><svg width="15" height="11" viewBox="0 0 20 14"><rect x="1" y="1" width="18" height="12" fill="none" stroke="#0d0d0d" stroke-width="2"/><path d="M1 1l9 7 9-7" fill="none" stroke="#0d0d0d" stroke-width="2"/></svg></span>
      info@ridgelinepavingco.com
    </li>
    <li class="contact-item">
      <span class="contact-icon"><svg width="12" height="16" viewBox="0 0 16 22"><path d="M8 1a7 7 0 0 0-7 7c0 5 7 13 7 13s7-8 7-13a7 7 0 0 0-7-7z" fill="#0d0d0d"/><circle cx="8" cy="8" r="2.6" fill="#f78f20"/></svg></span>
      418 Alder Way, Monterey CA
    </li>
    <li class="contact-item">
      <span class="contact-icon"><svg width="14" height="12" viewBox="0 0 20 16"><path d="M2 8l6 6L18 2" fill="none" stroke="#0d0d0d" stroke-width="3"/></svg></span>
      Lic#736920 · Licensed, Insured &amp; Bonded
    </li>
  </ul>

  <div class="brand-mark"><span class="brand-dot"></span><span>Ridgeline<br>Paving</span></div>

  <p class="web-address"><span class="web-dot"></span>ridgelinepavingco.com</p>
</section>

<section class="card card-back" aria-label="Card back">
  <svg class="card-shapes" viewBox="0 0 700 400" aria-hidden="true">
    <path d="M0 0 H230 C250 0 250 40 270 40 H0 Z" fill="var(--orange)"/>
    <path d="M700 300 C660 300 650 340 640 370 C635 390 620 400 600 400 H700 Z" fill="var(--white)"/>
  </svg>

  <h2 class="services-heading">Our Services</h2>
  <ul class="services-list">
    <li class="service">Asphalt construction and maintenance</li>
    <li class="service">Drainage</li>
    <li class="service">Foundations</li>
    <li class="service">Retaining walls</li>
    <li class="service">Chip seals</li>
    <li class="service">Excavation</li>
    <li class="service">Grading</li>
    <li class="service">Landscape</li>
    <li class="service">Ground work</li>
    <li class="service">Interlocking paver</li>
    <li class="service">Hydro-seeding</li>
    <li class="service">Structured and driveway demolition</li>
    <li class="service">Utility trenching and stump removal</li>
  </ul>

  <div class="brand-mark"><span class="brand-dot"></span><span>Ridgeline<br>Paving</span></div>
</section>

</body>
</html>
```